"Cedar Hollow Realty" is the name of my real estate company

This is for a: "for sale" sign, looking for a minimalist design, wire frame outline of a midcentury modern homes roof line or elevation?

My name is: Marcus Dunleavy (needed)
My Cell # is: 415 382 6094 (needed)
My BRE license # is: 02748156 (needed)
BRE needs to be displayed in this format: BRE 02748156 (needed)
The white outline on the sign riders 'pictured" may work on large sign
Note font on pictured rider sign
Updates

This design is for a real estate "for sale" sign or sandwich board sign. Do Not include the words "For Sale" on the sign.

The measurements are 36" inches (91.44 cm) Length, or tall X 24" inches (60.90 cm) Wide.

|
3
---- 24 ----
6
|

Sorry I wasn't more specific earlier. I'd like the elements of the sign to be scaled in size according to their importance, from largest to smallest:

My name: Marcus Dunleavy
My phone number: 415-382-6094
My company name: Cedar Hollow Realty
My license number: BRE 02748156 (This can be much smaller than the smallest text)
Additionally, please incorporate contemporary to mid-century modern elements on the wire frame roofline or a simple roof-like design.

Thank you!

Best regards,
Marcus

```html
<!DOCTYPE html>
<html lang="en">
<head>
<meta charset="utf-8">
<title>Cedar Hollow Realty – Marcus Dunleavy Yard Sign</title>
<link rel="stylesheet" href="https://fonts.googleapis.com/css2?family=Montserrat:wght@300;400&display=swap">
<style>
  :root {
    --backdrop: #666666;
    --post: #ffffff;
    --post-shade: #c4c4c6;
    --post-under: #d9d9d9;
    --post-under-shade: #a0a0a0;
    --panel: #000000;
    --ink: #ffffff;
    --roof-placeholder: #2a2a2a;
  }
  * { margin: 0; padding: 0; box-sizing: border-box; }
  html, body {
    width: 1200px;
    height: 1200px;
    overflow: hidden;
    background: var(--backdrop);
  }
  .canvas {
    position: relative;
    width: 1200px;
    height: 1200px;
    background: var(--backdrop);
    font-family: "Montserrat", sans-serif;
    color: var(--ink);
  }
  .post, .post-shade, .crossbar, .crossbar-shade, .post-under, .post-under-shade {
    position: absolute;
  }
  .post { left: 145px; top: 132px; width: 67px; height: 1068px; background: var(--post); }
  .post-shade { left: 212px; top: 132px; width: 12px; height: 1068px; background: var(--post-shade); }
  .crossbar-shade { left: 53px; top: 230px; width: 1076px; height: 79px; background: var(--post-shade); }
  .crossbar { left: 53px; top: 230px; width: 1076px; height: 66px; background: var(--post); }
  .post-under { left: 145px; top: 309px; width: 67px; height: 18px; background: var(--post-under); }
  .post-under-shade { left: 212px; top: 309px; width: 12px; height: 18px; background: var(--post-under-shade); }

  .sign-panel {
    position: absolute;
    left: 258px;
    top: 337px;
    width: 833px;
    height: 555px;
    background: var(--panel);
  }
  .sign-frame {
    position: absolute;
    left: 35px;
    top: 34px;
    width: 763px;
    height: 486px;
    border: 4px solid var(--ink);
  }
  .sign-text {
    position: absolute;
    left: 0;
    width: 100%;
    text-align: center;
    line-height: 1;
    white-space: nowrap;
  }
  .company-name {
    top: 61px;
    font-size: 34px;
    font-weight: 300;
    letter-spacing: 1px;
  }
  .company-tagline {
    top: 102px;
    font-size: 20px;
    font-weight: 300;
    letter-spacing: 22px;
    padding-left: 22px;
  }
  .roofline {
    position: absolute;
    left: 304px;
    top: 180px;
    width: 244px;
    height: 63px;
    background: var(--roof-placeholder);
  }
  .agent-name {
    top: 255px;
    font-size: 62px;
    font-weight: 400;
  }
  .agent-phone {
    top: 338px;
    font-size: 56px;
    font-weight: 400;
  }
  .license {
    top: 470px;
    font-size: 23px;
    font-weight: 300;
  }
</style>
</head>
<body>
  <main class="canvas">
    <div class="post"></div>
    <div class="post-shade"></div>
    <div class="crossbar-shade"></div>
    <div class="crossbar"></div>
    <div class="post-under"></div>
    <div class="post-under-shade"></div>

    <section class="sign-panel">
      <div class="sign-frame"></div>
      <p class="sign-text company-name">CEDAR HOLLOW</p>
      <p class="sign-text company-tagline">REALTY</p>
      <div class="roofline" role="img" aria-label="Mid-century modern roofline line drawing in white"></div>
      <h1 class="sign-text agent-name">MARCUS DUNLEAVY</h1>
      <p class="sign-text agent-phone">415-382-6094</p>
      <p class="sign-text license">BRE 02748156</p>
    </section>
  </main>
</body>
</html>
```